need eczema bath soak label/bag

need you to recreate this please. ai file. recreate this exact image please. ...if you want a big tip, create some different styles.

Colors
0054AA
0677BA
7BADD7
CADEEF
E8F1F8

```html
<!DOCTYPE html>
<html lang="en">
<head>
<meta charset="utf-8">
<title>The Ocean Healed My Bag – Bath Soak</title>
<link rel="stylesheet" href="https://fonts.googleapis.com/css2?family=Montserrat:wght@500;600;700;800&display=swap">
<style>
  :root {
    --backdrop: #e7eae3;
    --pouch-white: #f4f5f0;
    --foam: #eef3ee;
    --sea-light: #5fb894;
    --sea-deep: #1f7a60;
    --sand: #d9c3a3;
    --sand-deep: #c9ae8a;
    --ink: #1d4640;
    --zip: #dfe3dc;
  }
  html, body {
    margin: 0;
    padding: 0;
    width: 1182px;
    height: 1200px;
    overflow: hidden;
    background: var(--backdrop);
    font-family: "Montserrat", sans-serif;
  }
  .pouch {
    position: absolute;
    left: 243px;
    top: 149px;
    width: 695px;
    height: 934px;
    background: var(--pouch-white);
    border-radius: 6px;
    overflow: hidden;
  }
  .pouch-art {
    position: absolute;
    inset: 0;
    background: linear-gradient(180deg,
      var(--pouch-white) 0%,
      var(--pouch-white) 27%,
      var(--sea-light) 31%,
      var(--sea-deep) 38%,
      var(--sea-light) 44%,
      var(--foam) 50%,
      var(--foam) 55%,
      var(--sand) 62%,
      var(--sand-deep) 100%);
  }
  .zip-seal {
    position: absolute;
    left: 40px;
    right: 40px;
    top: 104px;
    height: 10px;
    border-top: 2px solid var(--zip);
    border-bottom: 2px solid var(--zip);
  }
  .label {
    position: absolute;
    inset: 0;
    text-align: center;
    color: var(--ink);
  }
  .title-kicker {
    position: absolute;
    top: 190px;
    width: 100%;
    font-size: 22px;
    font-weight: 700;
    letter-spacing: 4px;
  }
  .title {
    position: absolute;
    top: 240px;
    width: 100%;
    margin: 0;
    font-size: 50px;
    font-weight: 700;
    line-height: 67px;
    letter-spacing: 1px;
  }
  .blurb {
    position: absolute;
    top: 438px;
    width: 100%;
    font-size: 8.5px;
    font-weight: 600;
    line-height: 14px;
    letter-spacing: 0.5px;
  }
  .subtitle {
    position: absolute;
    top: 498px;
    width: 100%;
    font-size: 15px;
    font-weight: 600;
    letter-spacing: 1px;
  }
  .net-weight {
    position: absolute;
    top: 526px;
    width: 100%;
    font-size: 19px;
    font-weight: 600;
  }
  .product-type {
    position: absolute;
    top: 556px;
    width: 100%;
    font-size: 11px;
    font-weight: 600;
    letter-spacing: 1px;
  }
  .brand {
    position: absolute;
    top: 690px;
    width: 100%;
    display: flex;
    flex-direction: column;
    align-items: center;
    gap: 18px;
  }
  .brand-mark {
    width: 56px;
    height: 56px;
    background: var(--ink);
  }
  .brand-name {
    font-size: 17px;
    font-weight: 700;
    letter-spacing: 3px;
  }
  .footnote {
    position: absolute;
    top: 832px;
    width: 100%;
    font-size: 7px;
    font-weight: 600;
    letter-spacing: 1px;
  }
</style>
</head>
<body>
  <div class="pouch">
    <div class="pouch-art" role="img" aria-label="Watercolour ocean wave in greens breaking over pale sand"></div>
    <div class="zip-seal"></div>
    <div class="label">
      <div class="title-kicker">THE</div>
      <h1 class="title">OCEAN<br>HEALED<br>MY A BAG</h1>
      <div class="blurb">
        Warm mineral soak for dry,<br>
        itchy skin. Calming sea salts<br>
        soothe and soften daily.
      </div>
      <div class="subtitle">OCEAN IN A BAG</div>
      <div class="net-weight">NET WT 16 OZ</div>
      <div class="product-type">BATH SOAK</div>
      <div class="brand">
        <div class="brand-mark"></div>
        <div class="brand-name">TIDEWELL</div>
      </div>
      <div class="footnote">MADE WITH CARE</div>
    </div>
  </div>
</body>
</html>
```